Garage Door Sales and Repair Website

Looking for a website theme and home page design for a garage door sales and repair company (Cedar Ridge Overhead).   We have a new logo and color scheme (attached) and need to update our website to match.  Here is the current site http://www.cedarridgeoverhead.example/
The design should lend it self to being responsive and full screen.
I like this site (http://www.brightpane-studio.example/) how it has different color blocks and I would like to have a slide show on my home page as well.  4 slides utilizing some of the following concepts Garage Opener, Garage Doors, Springs, Garage Door Repair, Specials, Free Estimate, etc...
Would like color design to match logo / business cards attached.
Call for Free Estimate with phone number should be visible on top of the page as well.

Consumers
Professional Service
1 page
Other font styles liked:
- Oswald, Open Sans, other similar google web fonts

Requirements
Must have
- 4 slides for home page design
- Free Estimate
- Phone Number

Nice to have
- Call out for online specials

```html
<!DOCTYPE html>
<html lang="en">
<head>
<meta charset="utf-8">
<title>Cedar Ridge Overhead – Garage Door Sales and Repair</title>
<link href="https://fonts.googleapis.com/css2?family=Libre+Baskerville:wght@400;700&family=Open+Sans:wght@400;600;700;800&display=swap" rel="stylesheet">
<style>
:root{
  --slate:#48557e;
  --gold:#f2a640;
  --orange:#f7931e;
  --ink:#4a5578;
  --grey-card:#e3e3e3;
  --band:#3b3b3b;
  --foot:#242424;
  --foot-deep:#161616;
  --foot-text:#a8a8a8;
  --foot-head:#e88a2a;
}
*{margin:0;padding:0;box-sizing:border-box}
html,body{width:771px;height:1200px;overflow:hidden;background:#fff}
body{position:relative;font-family:"Open Sans",sans-serif;color:#555}
.abs{position:absolute}
.serif{font-family:"Libre Baskerville",serif}

/* header */
.site-header{left:0;top:0;width:771px;height:62px;background:var(--slate)}
.brand{left:110px;top:18px;color:#fff;font-family:"Libre Baskerville",serif;font-weight:700;font-size:11px;display:flex;align-items:center;gap:5px;width:110px;line-height:1.15}
.brand-dot{width:12px;height:12px;border-radius:50%;background:#fff;flex:none}
.top-contact{right:109px;top:7px;font-family:"Libre Baskerville",serif;font-size:7.3px;color:var(--gold);display:flex;gap:14px;align-items:center;white-space:nowrap}
.top-contact span{display:flex;align-items:center;gap:3px}
.nav{left:277px;top:47px;width:385px;display:flex;justify-content:space-between;font-family:"Libre Baskerville",serif;font-size:7.1px;color:#fff;white-space:nowrap}
.award{left:679px;top:5px;width:54px;height:54px;border-radius:50%;background:#6a6a6a}

/* hero */
.hero{left:0;top:62px;width:771px;height:230px;background:linear-gradient(100deg,#5c6670 0%,#c9ccd2 30%,#8a8f96 55%,#4d5258 80%,#3b4046 100%)}
.hero-panel{left:386px;top:90px;width:275px;height:172px;background:rgba(20,20,20,.85)}
.hero-title{left:394px;top:98px;font-size:17.5px;line-height:26px;color:var(--gold);text-transform:uppercase;font-weight:400;white-space:nowrap}
.hero-tags{left:393px;top:186px;font-size:6.4px;color:#fff;white-space:nowrap}
.hero-tags b{color:var(--orange);font-weight:400}
.btn{background:linear-gradient(#ffa72e,#f57f0c);color:#2b2b2b;font-family:"Libre Baskerville",serif;font-size:11.5px;display:flex;align-items:center;justify-content:center;border-radius:2px}
.hero-btn{left:393px;top:211px;width:148px;height:35px}
.dots{left:370px;top:273px;display:flex;gap:4px}
.dots i{width:4px;height:4px;border-radius:50%;background:#fff;display:block}
.dots i.on{background:var(--gold)}

/* services */
.services{left:110px;top:315px;width:551px;height:125px;display:flex}
.service{flex:1;background:linear-gradient(90deg,#f0f0f0,#cfcfcf);padding:8px 10px}
.service h3{font-family:"Libre Baskerville",serif;font-weight:400;font-size:10.6px;color:var(--ink);margin-bottom:10px;white-space:nowrap}
.service p{font-size:6.4px;line-height:11.6px;color:#555;height:62px}
.service a{font-size:8px;color:var(--ink);text-decoration:none;display:block;margin-top:9px}

/* specials */
.specials-title{left:0;top:475px;width:771px;text-align:center;font-size:19.5px;font-weight:700;color:var(--ink)}
.specials-sub{left:0;top:503px;width:771px;text-align:center;font-size:8px;color:var(--ink)}
.coupon{width:268px;height:124px;background:var(--grey-card);border:3px solid #f1f1f1;outline:1px solid #dcdcdc;padding:16px 15px}
.coupon .amt{font-weight:700;font-size:37px;color:var(--ink);line-height:40px;display:flex;align-items:baseline;gap:6px}
.coupon .amt small{font-size:15px;font-weight:700}
.coupon h4{font-weight:700;font-size:16px;color:var(--ink);margin-top:2px;letter-spacing:.3px}
.coupon p{font-size:7.3px;color:#333}
.note{left:0;top:810px;width:771px;text-align:center;font-size:7.2px;color:#333}
.cta-btn{left:312px;top:835px;width:147px;height:35px}

/* footer */
.badge-band{left:0;top:903px;width:771px;height:68px;background:var(--band)}
.badge-a{left:110px;top:928px;width:74px;height:27px;background:#111;border:1px solid #777;border-radius:3px}
.badge-b{left:198px;top:927px;width:31px;height:31px;border-radius:50%;background:#3a8fc8}
.follow{left:514px;top:937px;font-family:"Libre Baskerville",serif;font-size:7.5px;color:#bbb}
.social{top:927px;width:28px;height:28px;border-radius:4px}
.foot{left:0;top:971px;width:771px;height:192px;background:var(--foot)}
.foot-head{font-family:"Libre Baskerville",serif;font-size:7.3px;color:var(--foot-head)}
.foot-list{list-style:none;font-family:"Libre Baskerville",serif;font-size:6.8px;color:var(--foot-text)}
.foot-list li{height:19.2px}
.foot-list li::before{content:"▸ ";color:var(--orange);font-size:6px}
.view{font-family:"Libre Baskerville",serif;font-size:7.3px;color:var(--foot-head)}
.contact{left:570px;top:1024px;font-family:"Libre Baskerville",serif;font-size:6.8px;color:var(--foot-text);line-height:10.5px}
.copy-band{left:0;top:1163px;width:771px;height:37px;background:var(--foot-deep)}
.copy{left:0;top:1177px;width:771px;text-align:center;font-size:6.6px;color:#4e4e4e}
</style>
</head>
<body>

<header class="abs site-header"></header>
<div class="abs brand"><span class="brand-dot"></span>Cedar Ridge Overhead</div>
<div class="abs top-contact">
  <span><svg width="8" height="8" viewBox="0 0 10 10"><circle cx="5" cy="5" r="5" fill="#fff"/><path d="M3 2.5l1 1-.6.8c.4.8 1 1.4 1.8 1.8l.8-.6 1 1-.8 1C4.8 7.3 2.7 5.2 2.5 3.3z" fill="#48557e"/></svg>Contact Us Today: 720-555-0148</span>
  <span><svg width="9" height="7" viewBox="0 0 9 7"><rect width="9" height="7" fill="#fff"/><path d="M0 0l4.5 3.5L9 0" stroke="#48557e" fill="none"/></svg>hello@cedarridgeoverhead.example</span>
</div>
<nav class="abs nav"><span>HOME</span><span>OPENERS</span><span>GARAGE DOORS</span><span>BROKEN SPRINGS</span><span>GARAGE DOOR REPAIR</span><span>BLOG</span></nav>
<div class="abs award" role="img" aria-label="Award badge"></div>

<section class="abs hero" role="img" aria-label="Photo of a grey house with white two-car carriage garage doors at dusk"></section>
<div class="abs hero-panel"></div>
<h1 class="abs hero-title serif">Denver’s Preferred<br>Garage Door Sales and<br>Repair Company</h1>
<div class="abs hero-tags serif"><b>•</b>New Garage Doors &amp; Door Openers <b>•</b>Broken Springs <b>•</b>Garage Door Repairs</div>
<div class="abs btn hero-btn">Schedule Free Estimate</div>
<div class="abs dots"><i></i><i class="on"></i><i></i><i></i></div>

<section class="abs services">
  <article class="service"><h3>Garage Door Repair</h3><p>Cedar Ridge Overhead offers complete garage door repair and door maintenance services. Damaged panels, bent tracks, damaged rollers, broken springs...</p><a>READ MORE</a></article>
  <article class="service"><h3>Garage Door Openers</h3><p>Cedar Ridge Overhead offers a complete line of Garage Door Openers and accessories, from top makers like LiftPro and Gatewell. Whether you're...</p><a>READ MORE</a></article>
  <article class="service"><h3>New Garage Doors</h3><p>Cedar Ridge Overhead installs new garage doors. We will come to your home, take measurements, discuss your options, and give a free estimate...</p><a>READ MORE</a></article>
  <article class="service"><h3>Broken Springs</h3><p>Cedar Ridge Overhead is your local garage door spring replacement expert! We replace broken torsion springs, extension springs, and torque-style springs...</p><a>READ MORE</a></article>
</section>

<h2 class="abs specials-title serif">SAME DAY GARAGE DOOR REPAIR &amp; SERVICE</h2>
<p class="abs specials-sub serif">Fast – Affordable – Professional – No Additional Charge For Weekends – 24 Hour Emergency Service Available</p>

<div class="abs coupon" style="left:110px;top:529px"><div class="amt">$60<small>OFF</small></div><h4>SPRING REPLACEMENT</h4><p>$60 off Replacement of Two Garage Door Springs</p></div>
<div class="abs coupon" style="left:393px;top:529px"><div class="amt">$100<small>OFF</small></div><h4>NEW GARAGE DOOR</h4><p>Purchase and Installation of any Single Door</p></div>
<div class="abs coupon" style="left:110px;top:668px"><div class="amt">$200<small>OFF</small></div><h4>NEW GARAGE DOOR</h4><p>$200 off Purchase and Installation of any Double Door</p></div>
<div class="abs coupon" style="left:393px;top:668px"><div class="amt">$325<small>OVERHAUL</small></div><h4>BEST VALUE</h4><p>Overhaul includes new Springs, Rollers, Cables, Pulleys &amp; Bearings</p></div>

<p class="abs note">*** Must present / mention coupon at time of estimate. Not valid with other offers</p>
<div class="abs btn cta-btn">Schedule Free Estimate</div>

<div class="abs badge-band"></div>
<div class="abs badge-a" role="img" aria-label="Accreditation badge"></div>
<div class="abs badge-b" role="img" aria-label="Listing badge"></div>
<div class="abs follow">Follow Us On:</div>
<div class="abs social" style="left:568px;background:#777"></div>
<div class="abs social" style="left:601px;background:#3fa3c8"></div>
<div class="abs social" style="left:634px;background:#2b7fb8"></div>

<footer class="abs foot"></footer>
<div class="abs foot-head" style="left:110px;top:1000px">Garage Door Products &amp; Services</div>
<ul class="abs foot-list" style="left:112px;top:1024px"><li>Garage Door Repair</li><li>New Garage Doors</li><li>Garage Door Openers</li><li>Garage Door Maintenance</li><li>Garage Door Tune and Lube</li></ul>
<ul class="abs foot-list" style="left:237px;top:1024px"><li>Broken Springs</li><li>New Springs</li><li>Broken or Frayed Cables</li><li>Stuck / Off-Track Doors</li><li>Damaged Tracks &amp; Rollers</li></ul>
<div class="abs view" style="left:242px;top:1125px">View All</div>
<div class="abs foot-head" style="left:386px;top:1000px">Proudly Serving Denver Metro Area</div>
<ul class="abs foot-list" style="left:388px;top:1024px"><li>Arvada, CO</li><li>Aurora, CO</li><li>Berkley, CO</li><li>Boulder, CO</li><li>Brighton, CO</li></ul>
<ul class="abs foot-list" style="left:459px;top:1024px"><li>Broomfield, CO</li><li>Castle Pines, CO</li><li>Castle Rock, CO</li><li>Centennial, CO</li><li>Cherry Hills, CO</li></ul>
<div class="abs view" style="left:464px;top:1125px">View All</div>
<div class="abs foot-head" style="left:570px;top:1000px">Contact Information</div>
<div class="abs contact">Cedar Ridge Overhead<br>Juniper Row<br>Denver, CO 80099<br><br>
  <span style="display:flex;align-items:center;gap:3px;margin-top:3px"><svg width="7" height="7" viewBox="0 0 10 10"><circle cx="5" cy="5" r="5" fill="#ccc"/><path d="M3 2.5l1 1-.6.8c.4.8 1 1.4 1.8 1.8l.8-.6 1 1-.8 1C4.8 7.3 2.7 5.2 2.5 3.3z" fill="#242424"/></svg>720-555-0148</span>
  <span style="display:flex;align-items:center;gap:3px;margin-top:3px"><svg width="8" height="6" viewBox="0 0 9 7"><rect width="9" height="7" fill="#ccc"/><path d="M0 0l4.5 3.5L9 0" stroke="#242424" fill="none"/></svg>hello@cedarridgeoverhead.example</span>
</div>
<div class="abs copy-band"></div>
<p class="abs copy">Copyright © 2008 - 2016 Cedar Ridge Overhead Sales &amp; Repair, LLC. All rights reserved.</p>

</body>
</html>
```